Two wall artworks for physiotherapy clinic waiting room

We are a physiotherapy clinic located in Glebe, Sydney. We have a clinic that is within a beautiful heritage listed building and we have two blank white walls that need artwork. Each artwork will be 3000mm wide and 1200mm high. Our clinic is mostly white and I will include our brand's colours below. We are looking for bright, beautiful artworks that are consistent with our colours. One of the artworks should include our full logo including the text so that customers see the name of the clinic on their way into the waiting room. I will include our logo in the files below, as well as images of the clinic, the walls and some other signs that we have already. We would prefer artworks with nice patterns or graphics rather than images of people.

```html
<!DOCTYPE html>
<html lang="en">
<head>
<meta charset="utf-8">
<title>Wattle Lane Physio – Waiting Room Wall Artworks</title>
<link rel="stylesheet" href="https://fonts.googleapis.com/css2?family=Lexend:wght@400;500&display=swap">
<style>
  :root {
    --navy: #2a2470;
    --teal-deep: #1fa5a6;
    --teal: #2fb3b1;
    --teal-mid: #6ccac2;
    --teal-soft: #8fd5cd;
    --teal-pale: #c9ebe6;
    --aqua: #58c6cf;
    --white: #ffffff;
    --page: #ffffff;
  }
  * { margin: 0; padding: 0; box-sizing: border-box; }
  html, body {
    width: 1200px;
    height: 527px;
    overflow: hidden;
    background: var(--page);
  }
  .canvas {
    width: 1200px;
    height: 527px;
    display: flex;
    flex-direction: column;
    align-items: center;
    justify-content: center;
    gap: 14px;
  }
  .mural {
    display: block;
    width: 625px;
    height: 250px;
  }
  .brand-name {
    font-family: "Lexend", sans-serif;
    font-weight: 500;
    font-size: 66px;
    fill: var(--navy);
  }
  .brand-tagline {
    font-family: "Lexend", sans-serif;
    font-weight: 500;
    font-size: 23px;
    fill: var(--navy);
  }
  .service-label {
    font-family: "Lexend", sans-serif;
    font-weight: 400;
    font-size: 13px;
    fill: var(--navy);
  }
</style>
</head>
<body>
<main class="canvas">

  <!-- Artwork 1: clinic name wall -->
  <svg class="mural mural--name" viewBox="0 0 1000 400" role="img" aria-label="Wattle Lane Physio wall artwork">
    <rect width="1000" height="400" fill="var(--white)"/>
    <path class="wave wave--soft" fill="var(--teal-soft)"
      d="M700,0 H1000 V400 H600 C700,380 800,300 850,230 C900,160 885,90 810,50 C765,28 725,15 700,0Z"/>
    <path class="wave wave--pale" fill="var(--teal-pale)"
      d="M930,0 H1000 V260 C960,200 990,120 960,60 C950,35 940,15 930,0Z" opacity="0.7"/>
    <path class="wave wave--mid" fill="var(--teal-mid)"
      d="M170,340 C250,330 330,290 420,305 C500,320 560,360 650,345 C760,325 830,250 900,200 L1000,150 V400 H240Z"/>
    <path class="wave wave--deep" fill="var(--teal-deep)"
      d="M770,400 C850,360 900,290 1000,250 V400Z"/>
    <path class="wave wave--navy" fill="var(--navy)"
      d="M0,0 H230 C170,40 60,90 45,190 C35,280 130,330 220,345 C260,365 285,385 300,400 H0Z"/>
    <circle class="brand-dot" cx="295" cy="215" r="22" fill="var(--teal)"/>
    <text class="brand-name" x="340" y="232">Wattle Lane Physio</text>
    <text class="brand-tagline" x="343" y="274">Physiotherapy and Exercise Physiology</text>
  </svg>

  <!-- Artwork 2: services wall -->
  <svg class="mural mural--services" viewBox="0 0 1000 400" role="img" aria-label="Clinic services wall artwork">
    <rect width="1000" height="400" fill="var(--teal)"/>
    <path class="wave wave--aqua" fill="var(--aqua)"
      d="M0,0 H260 C210,50 130,70 70,120 L0,170Z"/>
    <path class="wave wave--soft" fill="var(--teal-soft)"
      d="M660,0 H1000 V120 C940,80 860,60 780,40 C720,25 690,10 660,0Z" opacity="0.6"/>
    <path class="blob blob--white" fill="var(--white)"
      d="M0,175 C60,125 150,85 260,88 C380,92 430,60 520,42 C600,28 660,90 750,96 C850,102 960,112 990,190 C1010,262 930,322 840,350 C780,370 700,385 600,400 H0Z"/>
    <path class="wave wave--mid" fill="var(--teal-mid)"
      d="M740,400 C850,380 940,340 1000,290 V400Z"/>
    <path class="wave wave--deep" fill="var(--teal-deep)"
      d="M900,400 C940,385 975,365 1000,345 V400Z"/>
    <path class="wave wave--navy" fill="var(--navy)"
      d="M0,270 C80,268 160,300 230,358 C262,384 300,395 370,400 H0Z"/>

    <g class="services">
      <g class="service">
        <circle cx="197" cy="188" r="41" fill="var(--teal)" role="img" aria-label="Physiotherapy icon"/>
        <text class="service-label" x="197" y="255" text-anchor="middle">Physiotherapy</text>
      </g>
      <g class="service">
        <circle cx="348" cy="188" r="41" fill="var(--navy)" role="img" aria-label="Exercise physiology icon"/>
        <text class="service-label" x="348" y="255" text-anchor="middle">Exercise</text>
        <text class="service-label" x="348" y="271" text-anchor="middle">Physiology</text>
      </g>
      <g class="service">
        <circle cx="500" cy="188" r="41" fill="var(--teal)" role="img" aria-label="Pain management icon"/>
        <text class="service-label" x="500" y="255" text-anchor="middle">Pain</text>
        <text class="service-label" x="500" y="271" text-anchor="middle">Management</text>
      </g>
      <g class="service">
        <circle cx="652" cy="188" r="41" fill="var(--navy)"/>
        <g class="icon icon--dumbbell" fill="none" stroke="var(--white)" stroke-width="3" stroke-linecap="round">
          <rect x="628" y="176" width="8" height="24" rx="3"/>
          <rect x="668" y="176" width="8" height="24" rx="3"/>
          <line x1="621" y1="188" x2="628" y2="188"/>
          <line x1="676" y1="188" x2="683" y2="188"/>
          <line x1="636" y1="188" x2="668" y2="188"/>
        </g>
        <text class="service-label" x="652" y="255" text-anchor="middle">Strength &amp;</text>
        <text class="service-label" x="652" y="271" text-anchor="middle">Rehab</text>
      </g>
      <g class="service">
        <circle cx="803" cy="188" r="41" fill="var(--teal)" role="img" aria-label="Wellbeing icon"/>
        <text class="service-label" x="803" y="255" text-anchor="middle">Move Well</text>
        <text class="service-label" x="803" y="271" text-anchor="middle">Live Well</text>
      </g>
    </g>
  </svg>

</main>
</body>
</html>
```